Event Production Company needs a Poster for a karaoke party

We need a poster similar to the one attached (the same typology of the logo), in which it can be seen that there are three prizes for the winners, a presenter and a jury. The room where the party is held is in Mirtel next Saturday, December 17, 2022. We are looking for an innovative poster, with a youthful air and a desire to party
Target Market(s)
Young people between 16 and 20 years old
Font styles to use
Other font styles liked:
- Pump Triline

Colors
E54698
E96AAD
F1A4CE
F9D9EA
FCEFF6
A7469A
B969AE
D3A5CF
EDDBEB
F8F0F9
6B429C
8869AF
B7A5CE
E3DAEB
F3F0F8
Requirements
Must have
- Fluorescent colors (neon), date, time and day of the event, the instagram profile has to appear

Nice to have
- that the gifts that are offered appear

Should not have
- little relevant information

```html
<!DOCTYPE html>
<html lang="es">
<head>
<meta charset="utf-8">
<title>Glow Karaoke – Mirtel</title>
<link rel="stylesheet" href="https://fonts.googleapis.com/css2?family=Monoton&family=Montserrat:wght@500;600;700&display=swap">
<style>
  :root {
    --stage: #6b6b6b;
    --night: #15122b;
    --violet: #3a2566;
    --plum: #6b429c;
    --magenta: #a7469a;
    --neon-pink: #e54698;
    --neon-soft: #f1a4ce;
    --blush: #f9d9ea;
    --gift-red: #e3273d;
    --gift-deep: #a8121f;
    --prize-yellow: #f5e33a;
    --logo-red: #a3343c;
    --white: #ffffff;
  }
  * { margin: 0; padding: 0; box-sizing: border-box; }
  html, body { width: 1200px; height: 2294px; overflow: hidden; }
  body { background: var(--stage); font-family: "Montserrat", sans-serif; position: relative; }

  .poster {
    position: absolute; left: 100px; top: 441px; width: 1000px; height: 1412px; overflow: hidden;
    background:
      radial-gradient(ellipse 420px 300px at 85% 70%, rgba(167,70,154,.55), transparent 70%),
      radial-gradient(ellipse 500px 380px at 20% 62%, rgba(107,66,156,.55), transparent 70%),
      radial-gradient(ellipse 600px 400px at 80% 20%, rgba(58,37,102,.7), transparent 70%),
      linear-gradient(170deg, #120f22 0%, #1e1838 40%, #2f1f55 70%, #251838 100%);
    box-shadow: 0 20px 40px rgba(0,0,0,.45);
  }
  .venue-badge {
    position: absolute; left: 268px; top: 61px; width: 466px; height: 96px;
    background: var(--white); border-radius: 16px;
    display: flex; align-items: center; justify-content: center;
    color: var(--logo-red); font-weight: 700; font-size: 66px; letter-spacing: 10px;
  }
  .headline {
    position: absolute; left: 0; width: 100%; text-align: center;
    font-family: "Monoton", sans-serif; font-weight: 400; line-height: 1;
  }
  .headline-top { top: 188px; font-size: 168px; color: var(--neon-pink);
    text-shadow: 0 0 10px rgba(229,70,152,.9), 0 0 26px rgba(229,70,152,.6); }
  .headline-bottom { top: 360px; font-size: 150px; color: var(--neon-soft); letter-spacing: -4px;
    text-shadow: 0 0 10px rgba(233,106,173,.9), 0 0 26px rgba(229,70,152,.6); }
  .details {
    position: absolute; left: 0; top: 556px; width: 100%; text-align: center;
    color: var(--blush); font-weight: 600; font-size: 35px; line-height: 58px; letter-spacing: .5px;
  }
  .mic { position: absolute; border-radius: 50%;
    background: radial-gradient(circle, rgba(136,105,175,.35), transparent 70%); }
  .mic-left { left: -20px; top: 600px; width: 160px; height: 260px; }
  .mic-right { right: -30px; top: 640px; width: 160px; height: 280px; }
  .gift {
    position: absolute; border-radius: 8px;
    background: linear-gradient(180deg, #ff4a5c 0%, var(--gift-red) 40%, var(--gift-deep) 100%);
    box-shadow: 0 0 30px rgba(229,70,152,.35);
  }
  .gift-first { left: 142px; top: 820px; width: 252px; height: 308px; }
  .gift-second { left: 438px; top: 876px; width: 207px; height: 247px; }
  .gift-third { left: 689px; top: 918px; width: 169px; height: 200px; }
  .rank {
    position: absolute; color: var(--white); font-weight: 600; font-size: 38px; line-height: 1;
  }
  .prize {
    position: absolute; top: 1130px; color: var(--prize-yellow); font-weight: 700; font-size: 40px;
    width: 200px; text-align: center;
  }
  .info-pill {
    position: absolute; left: 141px; top: 1195px; width: 719px; height: 58px;
    border: 2px solid rgba(255,255,255,.75); border-radius: 14px; display: flex; overflow: hidden;
  }
  .info-label { width: 358px; display: flex; align-items: center; justify-content: center;
    color: var(--white); font-weight: 500; font-size: 28px; }
  .info-handle { flex: 1; background: var(--white); display: flex; align-items: center; justify-content: center;
    color: var(--neon-pink); font-weight: 500; font-size: 29px; border-radius: 0 12px 12px 0; }
  .date-band {
    position: absolute; left: 0; top: 1275px; width: 100%; height: 81px; background: var(--neon-pink);
    display: flex; align-items: center; justify-content: center;
    color: var(--white); font-weight: 700; font-size: 44px;
  }
</style>
</head>
<body>
  <main class="poster">
    <div class="venue-badge">MIRTEL</div>

    <h1>
      <span class="headline headline-top">glow</span>
      <span class="headline headline-bottom">karaoke</span>
    </h1>

    <div class="mic mic-left" role="img" aria-label="Micrófono de neón decorativo"></div>
    <div class="mic mic-right" role="img" aria-label="Micrófono de neón decorativo"></div>

    <p class="details">
      PRESENTADO POR:<br>
      LARA MONTES Y NURIA VIDAL<br>
      JURADO PROFESIONAL<br>
      + 1000€ EN PREMIOS
    </p>

    <div class="gift gift-first" role="img" aria-label="Caja de regalo roja con lazo, primer premio">
      <span class="rank" style="right:26px; bottom:44px;">1</span>
    </div>
    <div class="gift gift-second" role="img" aria-label="Caja de regalo roja con lazo, segundo premio">
      <span class="rank" style="right:20px; bottom:30px;">2</span>
    </div>
    <div class="gift gift-third" role="img" aria-label="Caja de regalo roja con lazo, tercer premio">
      <span class="rank" style="right:12px; bottom:28px;">3</span>
    </div>

    <span class="prize" style="left:158px;">500€</span>
    <span class="prize" style="left:433px;">300€</span>
    <span class="prize" style="left:668px;">150€</span>

    <div class="info-pill">
      <span class="info-label">TODA LA INFO :</span>
      <span class="info-handle">@GLOWKARAOKE</span>
    </div>

    <div class="date-band">sábado, 17 de diciembre de 2022</div>
  </main>
</body>
</html>
```